Design outside banner for my business

We are looking for someone to design a promotional banner we will put in different places in our city to promote our car finance business. Important that we keep a white background. Size is 96 inches wide by 48 inches high

Requirements
Must have
• White background and large logo
Should not have
• Small text

```html
<!DOCTYPE html>
<html lang="fr">
<head>
<meta charset="utf-8">
<title>Valmont Auto Crédit – Bannière extérieure</title>
<link rel="stylesheet" href="https://fonts.googleapis.com/css2?family=Roboto+Condensed:wght@700&family=Exo+2:ital,wght@1,800&display=swap">
<style>
  :root {
    --red: #e8232e;
    --blue: #2f5db3;
    --blue-text: #2c55a8;
    --grey-box: #e4e6ea;
    --white: #f7f7f7;
    --ink: #2a2b2e;
    --stage: #dcdcdc;
    --mascot-orange: #ef7a2a;
    --mascot-blue: #4a5fb0;
  }
  * { margin: 0; padding: 0; box-sizing: border-box; }
  html, body { width: 1200px; height: 815px; overflow: hidden; }
  body {
    background: var(--stage);
    font-family: "Roboto Condensed", "Arial Narrow", sans-serif;
    font-weight: 700;
    position: relative;
  }
  .banner {
    position: absolute;
    left: 30px; top: 140px;
    width: 1140px; height: 536px;
    background: var(--white);
    overflow: hidden;
  }
  .band { position: absolute; left: 0; width: 100%; }
  .band--top { top: 0; height: 33px; }
  .band--bottom { bottom: 0; height: 60px; }

  .tag-box {
    position: absolute; left: 0;
    background: var(--grey-box);
    color: var(--blue-text);
    display: flex; align-items: center;
    padding-left: 20px;
    font-size: 27px;
    height: 53px;
    white-space: nowrap;
  }
  .tag-box--rank { top: 51px; width: 176px; }
  .tag-box--chance { top: 109px; width: 268px; }
  .tag-box--finance { top: 169px; width: 580px; }
  .tag-box--finance .emph { margin-left: 6px; }

  .situations {
    position: absolute; left: 54px; top: 235px;
    list-style: none;
  }
  .situations li {
    display: flex; align-items: center;
    height: 27.6px;
    color: var(--red);
    font-size: 25px;
    white-space: nowrap;
  }
  .situations svg { width: 20px; height: 20px; margin-right: 17px; flex: none; }

  .brand {
    position: absolute; left: 652px; top: 84px;
    color: var(--ink);
    font-size: 52px;
    line-height: 58px;
    text-transform: uppercase;
    white-space: nowrap;
  }
  .brand span { display: block; }
  .mascot {
    position: absolute; left: 960px; top: 12px;
    width: 160px; height: 210px;
    border-radius: 40px 40px 20px 20px;
    background: linear-gradient(180deg, var(--mascot-orange) 0%, var(--mascot-orange) 55%, var(--mascot-blue) 100%);
  }
  .tagline {
    position: absolute; right: 23px; top: 238px;
    color: var(--red);
    font-size: 22px;
    white-space: nowrap;
  }
  .perks {
    position: absolute; right: 23px; top: 285px;
    list-style: none; text-align: right;
  }
  .perks li {
    display: flex; justify-content: flex-end; align-items: center;
    height: 36.5px;
    color: var(--blue-text);
    font-size: 25px;
    white-space: nowrap;
  }
  .perks svg { width: 26px; height: 18px; margin-left: 20px; }
  .phone {
    position: absolute; right: 28px; top: 408px;
    color: var(--red);
    font-family: "Exo 2", "Arial Black", sans-serif;
    font-style: italic; font-weight: 800;
    font-size: 48px;
    letter-spacing: 7px;
    white-space: nowrap;
  }
  .website {
    position: absolute; left: 28px; bottom: 12px;
    color: #fff;
    font-family: "Exo 2", "Arial Black", sans-serif;
    font-style: italic; font-weight: 800;
    font-size: 29px;
    letter-spacing: 4px;
    text-transform: uppercase;
    white-space: nowrap;
  }
</style>
</head>
<body>
  <main class="banner">
    <svg class="band band--top" viewBox="0 0 1140 33" preserveAspectRatio="none" aria-hidden="true">
      <rect width="1140" height="33" fill="var(--red)"/>
      <g fill="var(--white)">
        <polygon points="540,0 556,0 580,33 564,33"/>
        <polygon points="600,0 618,0 642,33 624,33"/>
        <polygon points="665,0 685,0 709,33 689,33"/>
        <polygon points="735,0 757,0 781,33 759,33"/>
        <polygon points="810,0 834,0 858,33 834,33"/>
        <polygon points="890,0 916,0 940,33 914,33"/>
        <polygon points="975,0 1003,0 1027,33 999,33"/>
        <polygon points="1065,0 1095,0 1119,33 1089,33"/>
      </g>
    </svg>

    <div class="tag-box tag-box--rank">1RE, 2E, 3E</div>
    <div class="tag-box tag-box--chance">CHANCE AU CRÉDIT</div>
    <div class="tag-box tag-box--finance">Financement automobile <span class="emph">AUCUN CAS REFUSÉ</span></div>

    <ul class="situations">
      <li><svg viewBox="0 0 20 20"><circle cx="10" cy="10" r="10" fill="var(--blue)"/><path d="M5.5 10.2l3 3 6-6" stroke="#fff" stroke-width="2.4" fill="none"/></svg>Proposition au consommateur</li>
      <li><svg viewBox="0 0 20 20"><circle cx="10" cy="10" r="10" fill="var(--blue)"/><path d="M5.5 10.2l3 3 6-6" stroke="#fff" stroke-width="2.4" fill="none"/></svg>Remise volontaire</li>
      <li><svg viewBox="0 0 20 20"><circle cx="10" cy="10" r="10" fill="var(--blue)"/><path d="M5.5 10.2l3 3 6-6" stroke="#fff" stroke-width="2.4" fill="none"/></svg>Retards de paiements</li>
      <li><svg viewBox="0 0 20 20"><circle cx="10" cy="10" r="10" fill="var(--blue)"/><path d="M5.5 10.2l3 3 6-6" stroke="#fff" stroke-width="2.4" fill="none"/></svg>Recouvrements</li>
      <li><svg viewBox="0 0 20 20"><circle cx="10" cy="10" r="10" fill="var(--blue)"/><path d="M5.5 10.2l3 3 6-6" stroke="#fff" stroke-width="2.4" fill="none"/></svg>Faible revenu</li>
      <li><svg viewBox="0 0 20 20"><circle cx="10" cy="10" r="10" fill="var(--blue)"/><path d="M5.5 10.2l3 3 6-6" stroke="#fff" stroke-width="2.4" fill="none"/></svg>Récemment travailleur autonome</li>
      <li><svg viewBox="0 0 20 20"><circle cx="10" cy="10" r="10" fill="var(--blue)"/><path d="M5.5 10.2l3 3 6-6" stroke="#fff" stroke-width="2.4" fill="none"/></svg>Faillite</li>
      <li><svg viewBox="0 0 20 20"><circle cx="10" cy="10" r="10" fill="var(--blue)"/><path d="M5.5 10.2l3 3 6-6" stroke="#fff" stroke-width="2.4" fill="none"/></svg>Mauvais crédit</li>
    </ul>

    <div class="brand"><span>Valmont</span><span>Auto Crédit</span></div>
    <div class="mascot" role="img" aria-label="Mascotte illustrée de l'entreprise tenant une clé de voiture"></div>

    <p class="tagline">LES SPÉCIALISTE DU FINANCEMENT AUTOMOBILE!</p>

    <ul class="perks">
      <li>Réponse Rapide<svg viewBox="0 0 26 18"><path d="M0 9h18M12 2l8 7-8 7" stroke="var(--red)" stroke-width="4" fill="none"/></svg></li>
      <li>100% Approbation<svg viewBox="0 0 26 18"><path d="M0 9h18M12 2l8 7-8 7" stroke="var(--red)" stroke-width="4" fill="none"/></svg></li>
      <li>Faites Vous Préapprouver<svg viewBox="0 0 26 18"><path d="M0 9h18M12 2l8 7-8 7" stroke="var(--red)" stroke-width="4" fill="none"/></svg></li>
    </ul>

    <p class="phone">514-555-0182</p>

    <svg class="band band--bottom" viewBox="0 0 1140 60" preserveAspectRatio="none" aria-hidden="true">
      <rect width="1140" height="60" fill="var(--blue)"/>
      <g fill="var(--white)">
        <polygon points="905,0 925,0 968,60 948,60"/>
        <polygon points="945,0 967,0 1010,60 988,60"/>
        <polygon points="990,0 1014,0 1057,60 1033,60"/>
        <polygon points="1040,0 1066,0 1109,60 1083,60"/>
        <polygon points="1095,0 1123,0 1140,24 1140,60 1138,60"/>
      </g>
    </svg>
    <p class="website">www.valmontautocredit.com</p>
  </main>
</body>
</html>
```